Marlow Haven

Yoga and Pilates
I teach privates and small groups

Simple clean design 2-4 pages.
(Bookings will be though contacting me, so need for booking capabilities)

```html
<!DOCTYPE html>
<html lang="en">
<head>
<meta charset="utf-8">
<title>Marlow Haven — Yoga &amp; Pilates</title>
<link rel="stylesheet" href="https://fonts.googleapis.com/css2?family=Poppins:wght@400;500;600&display=swap">
<style>
  :root {
    --coral: #ef9f8a;
    --ink: #111111;
    --text: #222222;
    --muted: #444444;
    --white: #ffffff;
    --services-bg: #bbbbbb;
    --about-bg: #fcf0ee;
    --rule: #dddddd;
  }
  * { margin: 0; padding: 0; box-sizing: border-box; }
  html, body { width: 1200px; height: 2314px; overflow: hidden; }
  body { position: relative; font-family: "Poppins", sans-serif; color: var(--text); background: var(--white); }
  .abs { position: absolute; }

  /* Hero */
  .hero { position: absolute; left: 0; top: 0; width: 1200px; height: 666px; }
  .hero-photo { position: absolute; inset: 0;
    background: linear-gradient(100deg, #f2efe6 0%, #ddd6c6 35%, #c8bca6 60%, #b3a58c 85%, #9d8f77 100%); }
  .hero-floor { position: absolute; left: 0; bottom: 0; width: 100%; height: 60px;
    background: linear-gradient(180deg, #5e5243 0%, #a8895e 30%, #c9a77a 100%); }
  .brand { font-weight: 500; color: var(--coral); line-height: 1; }
  .nav-logo { left: 112px; top: 38px; font-size: 32px; }
  .nav-links { display: flex; gap: 30px; left: 437px; top: 44px; font-size: 16px; color: var(--ink); }
  .btn { display: flex; align-items: center; justify-content: center; background: var(--coral); color: var(--white); border-radius: 4px; font-size: 17px; }
  .nav-btn { left: 923px; top: 32px; width: 165px; height: 46px; }
  .hero-title { left: 110px; top: 274px; font-size: 52px; font-weight: 500; color: var(--ink); line-height: 1.2; }
  .hero-text { left: 113px; top: 350px; width: 400px; font-size: 15.5px; line-height: 29px; color: var(--ink); }
  .hero-link { left: 112px; top: 424px; font-size: 17px; font-weight: 500; color: var(--ink); border-bottom: 1.5px solid var(--ink); line-height: 1.3; }

  /* Services */
  .services { position: absolute; left: 0; top: 666px; width: 1200px; height: 616px; background: var(--services-bg); }
  .section-title { position: absolute; width: 100%; text-align: center; font-weight: 600; }
  .services-title { top: 66px; font-size: 38px; color: var(--white); }
  .service-photo { position: absolute; top: 144px; width: 462px; height: 357px; border-radius: 8px; }
  .photo-private { left: 123px; background: linear-gradient(135deg, #8c8577 0%, #6a5f55 45%, #c49a62 100%); }
  .photo-groups { left: 615px; background: linear-gradient(160deg, #3c4a3d 0%, #6f7d68 40%, #b58a5e 80%, #8a6a86 100%); }
  .service-label { position: absolute; top: 510px; width: 462px; text-align: center; font-size: 25px; font-weight: 600; color: var(--white); }

  /* About */
  .about { position: absolute; left: 0; top: 1282px; width: 1200px; height: 343px; background: var(--about-bg); }
  .about-title { left: 153px; top: 78px; font-size: 30px; font-weight: 600; color: var(--ink); }
  .about-text { left: 148px; top: 133px; width: 670px; font-size: 15.5px; line-height: 32px; color: var(--ink); }
  .about-btn { left: 887px; top: 146px; width: 165px; height: 46px; }

  /* Newsletter */
  .newsletter { position: absolute; left: 0; top: 1625px; width: 1200px; height: 428px; }
  .newsletter-photo { position: absolute; inset: 0;
    background: linear-gradient(90deg, #3b3a3a 0%, #5d5a57 30%, #6e6863 55%, #4a4c52 80%, #3a3c42 100%); }
  .newsletter-shade { position: absolute; left: 0; bottom: 0; width: 100%; height: 100px;
    background: linear-gradient(180deg, rgba(40,70,90,0) 0%, rgba(40,80,105,0.55) 100%); }
  .newsletter-title { top: 131px; font-size: 34px; color: var(--white); }
  .newsletter-sub { position: absolute; top: 182px; width: 100%; text-align: center; font-size: 16.5px; color: var(--white); }
  .field { position: absolute; top: 237px; height: 52px; background: var(--white); border-radius: 2px;
    font-size: 14.5px; color: var(--text); display: flex; align-items: center; padding-left: 16px; }
  .field-first { left: 180px; width: 225px; }
  .field-last { left: 421px; width: 224px; }
  .field-email { left: 659px; width: 224px; }
  .signup-btn { left: 900px; top: 237px; width: 120px; height: 52px; font-weight: 600; border-radius: 2px; }

  /* Footer */
  .footer-logo { left: 114px; top: 2102px; font-size: 38px; }
  .footer-col { font-size: 15px; line-height: 30.5px; color: var(--muted); }
  .footer-contact { left: 470px; top: 2100px; }
  .footer-links { left: 726px; top: 2100px; }
  .social { display: flex; gap: 9px; left: 956px; top: 2109px; }
  .social span { width: 38px; height: 38px; border: 1px solid #555; border-radius: 50%; }
  .footer-rule { left: 112px; top: 2249px; width: 977px; height: 1px; background: var(--rule); }
  .copyright { left: 0; top: 2270px; width: 1200px; text-align: center; font-size: 15px; color: var(--ink); }
</style>
</head>
<body>

<header class="hero">
  <div class="hero-photo" role="img" aria-label="Woman in a seated yoga stretch beside a laptop in a bright, plain studio"></div>
  <div class="hero-floor" role="img" aria-label="Wooden studio floor"></div>
  <div class="abs brand nav-logo">Marlow Haven</div>
  <nav class="abs nav-links">
    <span>About</span><span>Our Instructors</span><span>Classes</span><span>Location</span><span>Blog</span>
  </nav>
  <div class="abs btn nav-btn">Book a Class</div>
  <h1 class="abs hero-title">Marlow Haven</h1>
  <p class="abs hero-text">Sed ut perspiciatis unde omnis iste natus eor sit voluptatem accusantium doloremque</p>
  <span class="abs hero-link">Get Started</span>
</header>

<section class="services">
  <h2 class="section-title services-title">Our Services</h2>
  <div class="service-photo photo-private" role="img" aria-label="Instructor guiding a client on a pilates reformer"></div>
  <div class="service-label" style="left:123px">Private Teaching</div>
  <div class="service-photo photo-groups" role="img" aria-label="Small group seated in yoga pose with hands raised"></div>
  <div class="service-label" style="left:615px">Small Groups</div>
</section>

<section class="about">
  <h2 class="abs about-title">About Marlow Haven</h2>
  <p class="abs about-text">Sed ut perspiciatis unde omnis iste natus error sit uptatem accusantium doloremque laudantium, totam rem aperiam, eaque ipsa quae ab illo inventore veritatis et quasi architecto beatae vitae dicta sunt explicabo. Nemo enim ipsam voluptatem quia voluptas sit aspernatur aut</p>
  <div class="abs btn about-btn">Learn More</div>
</section>

<section class="newsletter">
  <div class="newsletter-photo" role="img" aria-label="Yoga class stretching on mats in a studio"></div>
  <div class="newsletter-shade"></div>
  <h2 class="section-title newsletter-title">Subscribe to Our Newsletter</h2>
  <p class="newsletter-sub">Sign up to receive news and updates.</p>
  <div class="field field-first">First Name</div>
  <div class="field field-last">Last Name</div>
  <div class="field field-email">Email Address</div>
  <div class="abs btn signup-btn">Sign Up</div>
</section>

<footer>
  <div class="abs brand footer-logo">Marlow Haven</div>
  <div class="abs footer-col footer-contact">48 Willow Lane<br>Harbourside, NZ<br>(555) 014-2287</div>
  <div class="abs footer-col footer-links">About<br>Location<br>Classes<br>Book a Class</div>
  <div class="abs social" aria-label="Social links"><span></span><span></span><span></span></div>
  <div class="abs footer-rule"></div>
  <p class="abs copyright">©Copyright ©2022 Marlow Haven. All Rights Reserved.</p>
</footer>

</body>
</html>
```